LKT business card design

Coastal Guard Auxiliary Kin Services exists to provide timely and relevant programs and services to assist commanders with their role to ensure their assigned Families (Soldiers, spouses, children, significant others) have the highest possible level of well-being, and are the "ready" (for deployment, family separation, and self-sufficiency during that separation). We accomplish this task through several functional areas: Leadership (Director), Coordination (Coordinator--coordinates a variety of human services, staff sections, sister agencies, etc. to offer training and support), unit Family Readiness Programs, Junior Learner and Campus Aid, Bereaved Contact Network, Lantern Path Initiative (deployment and reintegration training), Recovery Care (for wounded warriors), Crisis Intervention, and Prevention Education and Training. Our aim is to demonstrate "Kin Above All" in everything we do, because Family Readiness improves Soldier Readiness which improves Army Readiness.

Folks, I've tried to upload the logos I mentioned, with not luck. You can get a look at one version of the Guard Auxiliary Kin Services logo at www.gaks-example.org.

Reason: Extendinig a couple days because I've not yet had any sucess uploading logos I mention in the brief. Hoping to crack the nut on that soon Thanks for your patient work.

Target Market(s)

Army Reserve Commanders, First Sergeants, Adult & Youth Volunteers & Family Members who are called to contribute to Whole Guard Kin readiness by being skilled at handling the challendes of deployment, family separation, and the self-sufficiency required when their Soldier deploys (e.g., fulfilling the Soldiers roles on the homefront while he or she is away)

Industry/Entity Type

Training

Contact Information for Business Card

Dr. Marcus T. Holloway, Director
Family Programs, 4th RDG, CGAWEST
2846 Ridge Lane
Honolulu, HI 96502-4718
808-555-0172 ext. 4820
BB: 808-555-0639
marcus.t.holloway7.staff@postbox-example.net

Requirements
Must have
• Family Programs Logo with text
Nice to have
• 4th RDG and CGAWEST Logo
Should not have
• old GAKS Logo (Green, blue globe with family silhouette)

```html
<!DOCTYPE html>
<html lang="en">
<head>
<meta charset="utf-8">
<title>LKT Business Card – Dr. Marcus T. Holloway</title>
<link rel="stylesheet" href="https://fonts.googleapis.com/css2?family=Questrial&family=Arimo:wght@400&display=swap">
<style>
  :root {
    --card-white: #ffffff;
    --band-green: #56b72f;
    --title-green: #4ea735;
    --ink-dark: #2b2b2b;
    --text-on-green: #ffffff;
  }
  html, body {
    margin: 0;
    padding: 0;
    width: 1200px;
    height: 682px;
    overflow: hidden;
    background: var(--card-white);
  }
  .card {
    position: relative;
    width: 1200px;
    height: 682px;
    background: var(--card-white);
    overflow: hidden;
  }
  .mark {
    position: absolute;
    display: flex;
    align-items: center;
    gap: 10px;
    font-family: "Questrial", sans-serif;
    font-weight: 400;
    color: var(--ink-dark);
    text-align: center;
    line-height: 1.15;
  }
  .mark-left { left: 48px; top: 40px; font-size: 22px; }
  .mark-center { left: 480px; top: 30px; width: 250px; font-size: 22px; flex-direction: column; gap: 8px; }
  .mark-right { right: 40px; top: 38px; font-size: 22px; flex-direction: column; gap: 8px; }
  .mark-shape-square { width: 60px; height: 60px; background: var(--ink-dark); }
  .mark-shape-circle { width: 58px; height: 58px; border-radius: 50%; background: var(--title-green); }
  .mark-shape-circle.badge { background: #c8102e; }

  .identity {
    position: absolute;
    left: 0;
    width: 1200px;
    top: 186px;
    text-align: center;
    font-family: "Questrial", sans-serif;
    color: var(--title-green);
    font-size: 49px;
    line-height: 74px;
  }
  .identity p { margin: 0; }

  .contact-band {
    position: absolute;
    left: 0;
    top: 357px;
    width: 1200px;
    height: 325px;
    background: var(--band-green);
  }
  .contact-row {
    position: absolute;
    left: 150px;
    display: flex;
    align-items: flex-start;
    font-family: "Arimo", sans-serif;
    color: var(--text-on-green);
    font-size: 35px;
    line-height: 46px;
  }
  .contact-row svg { width: 34px; height: 34px; margin-top: 6px; flex: none; }
  .contact-text { margin-left: 40px; }
  .row-address { top: 32px; }
  .row-phone { top: 170px; }
  .row-email { top: 240px; }
</style>
</head>
<body>
<main class="card">
  <div class="mark mark-left">
    <span class="mark-shape-square" aria-hidden="true"></span>
    <span>HARBOR<br>CORPS</span>
  </div>
  <div class="mark mark-center">
    <span class="mark-shape-circle" aria-hidden="true"></span>
    <span>Guard Auxiliary Kin Services</span>
  </div>
  <div class="mark mark-right">
    <span class="mark-shape-circle badge" aria-hidden="true"></span>
    <span>4th RDG</span>
  </div>

  <section class="identity">
    <p class="person-name">Dr. Marcus T. Holloway</p>
    <p class="person-role">Director Family Programs</p>
  </section>

  <section class="contact-band">
    <div class="contact-row row-address">
      <svg viewBox="0 0 24 24" aria-hidden="true"><path fill="#fff" d="M12 2a7 7 0 0 0-7 7c0 5 7 13 7 13s7-8 7-13a7 7 0 0 0-7-7zm0 9.5A2.5 2.5 0 1 1 12 6.5a2.5 2.5 0 0 1 0 5z"/></svg>
      <div class="contact-text">4th RDG, CGAWEST<br>2846 Ridge Lane Honolulu, HI &nbsp;- 96502-4718</div>
    </div>
    <div class="contact-row row-phone">
      <svg viewBox="0 0 24 24" aria-hidden="true"><rect x="6.5" y="2" width="11" height="20" rx="2" fill="none" stroke="#fff" stroke-width="2"/><circle cx="12" cy="18" r="1.2" fill="#fff"/></svg>
      <div class="contact-text">808-555-0172 &nbsp;ext. 4820 &nbsp;BB: 808-555-0639</div>
    </div>
    <div class="contact-row row-email">
      <svg viewBox="0 0 24 24" aria-hidden="true"><rect x="2.5" y="5" width="19" height="14" fill="none" stroke="#fff" stroke-width="2"/><path d="M3 6l9 7 9-7" fill="none" stroke="#fff" stroke-width="2"/></svg>
      <div class="contact-text">marcus.t.holloway7.staff@postbox-example.net</div>
    </div>
  </section>
</main>
</body>
</html>
```